Company or website name
- The Steadfast Haulers and Storage
- Links to the website
- Brightcarryhaul.com
- Describe your company and organization and target audience
- Residential and commercial moving and relocation service that needs a website redesign.
- The design should have the following
- I NEED THE WEBSITE TO BE SIMPLE AND STRAIGHT TO THE POINT...MAIN CONCERN IS THAT THEY FILL OUT INFORMATION TO GET QUOTE. SITE EXAMPLE THAT I LIKE IS ( WWW.GOTORVALE.COM) https://www.quornhaulwaysco.com/

```html
<!DOCTYPE html>
<html lang="en">
<head>
<meta charset="utf-8">
<title>The Steadfast Haulers and Storage</title>
<link href="https://fonts.googleapis.com/css2?family=Montserrat:ital,wght@0,500;0,600;0,700;0,800;1,700&family=Open+Sans:ital,wght@0,400;0,600;0,700;1,400;1,600&display=swap" rel="stylesheet">
<style>
:root{
  --blue:#1b6fc4;
  --blue-dark:#135aa3;
  --navy:#0f2a4a;
  --orange:#f7a541;
  --ink:#2b2f36;
  --muted:#6b7280;
  --line:#e5e7eb;
  --paper:#ffffff;
  --soft:#f3f4f6;
}
*{box-sizing:border-box;margin:0;padding:0}
html,body{width:1200px;height:2804px;overflow:hidden;background:var(--paper)}
body{position:relative;font-family:"Open Sans",Arial,sans-serif;color:var(--ink);font-size:13px;line-height:1.55}
h1,h2,h3,h4{font-family:"Montserrat",Arial,sans-serif}

/* brand (text name only) */
.brand-name{font-family:"Montserrat",sans-serif;font-weight:700;font-size:22px;color:var(--blue);white-space:nowrap}

/* header */
.site-header{position:absolute;left:0;top:0;width:1200px;height:95px;background:var(--paper);z-index:3}
.site-header .brand{position:absolute;left:48px;top:30px}
.brand-tag{position:absolute;left:48px;top:62px;font-size:10px;color:var(--muted)}
.topline{position:absolute;right:50px;top:10px;font-size:10px;color:var(--muted)}
.main-nav{position:absolute;right:50px;top:44px;display:flex;gap:22px;font-family:"Montserrat",sans-serif;font-size:10px;font-weight:600;text-transform:uppercase;color:var(--ink)}
.main-nav .active{color:var(--blue)}

/* hero */
.hero{position:absolute;left:0;top:95px;width:1200px;height:570px}
.hero-photo{position:absolute;inset:0;background:linear-gradient(180deg,#bcd3e8 0%,#e6eef5 45%,#c9ccd1 72%,#8c9198 100%)}
.hero-copy{position:absolute;left:150px;top:318px;width:560px;text-align:center}
.hero-copy h1{font-size:27px;font-weight:700;color:var(--navy)}
.hero-copy p{font-size:12px;color:#334155;font-style:italic}
.call-box{position:absolute;left:0;top:395px;width:450px;height:150px;background:var(--blue);padding:28px 0 0 50px;color:#fff}
.call-box span{display:block;font-style:italic;font-weight:600;font-size:15px}
.call-box strong{display:block;font-family:"Montserrat",sans-serif;font-size:42px;font-weight:700;line-height:1.2}
.hero-rule{position:absolute;left:0;top:665px;width:1200px;height:8px;background:var(--orange)}

/* quote form */
.quote-form{position:absolute;left:800px;top:107px;width:380px;height:560px;background:var(--blue);padding:24px 26px;color:#fff;z-index:2;box-shadow:0 6px 18px rgba(0,0,0,.2)}
.quote-form h2{font-size:24px;font-weight:800;line-height:1.15;text-transform:uppercase}
.quote-form h2 em{font-style:italic;background:var(--orange);padding:0 6px;color:#fff}
.tabs{display:flex;gap:6px;margin:18px 0 16px}
.tab{flex:1;height:62px;background:var(--blue-dark);display:flex;flex-direction:column;align-items:center;justify-content:center;gap:4px;font-size:10px;font-weight:600}
.tab.on{background:#fff;color:var(--blue)}
.tab i{width:20px;height:16px;border:2px solid currentColor;border-radius:2px;display:block}
.field-row{display:flex;gap:10px;margin-bottom:10px}
.field{flex:1}
.field label{display:block;font-size:10px;margin-bottom:3px}
.field div{height:32px;background:#fff;border-radius:2px;color:var(--muted);font-size:11px;padding:7px 9px}
.form-actions{display:flex;gap:10px;margin-top:18px}
.btn{display:inline-block;font-family:"Montserrat",sans-serif;font-weight:700;font-size:11px;text-align:center;padding:11px 0;border-radius:2px}
.btn-orange{flex:1;background:var(--orange);color:#fff}
.btn-light{flex:1;background:#fff;color:var(--blue)}

/* about */
.about{position:absolute;left:0;top:673px;width:1200px;height:540px}
.about-panel{position:absolute;left:520px;top:80px;width:680px;height:240px;background:var(--soft)}
.about-photo{position:absolute;left:560px;top:45px;width:510px;height:330px;background:linear-gradient(135deg,#e9dccb,#c9a77f 55%,#8b6b4a)}
.about-copy{position:absolute;left:50px;top:95px;width:420px}
.about-copy h2{font-size:24px;font-weight:700;color:var(--blue);line-height:1.25;margin-bottom:18px}
.about-copy p{font-size:11.5px;color:var(--muted);margin-bottom:12px}

/* services */
.services{position:absolute;left:0;top:1215px;width:1200px;height:468px;background:var(--orange)}
.services h2{position:absolute;left:140px;top:36px;font-size:22px;font-weight:700;color:var(--ink)}
.services .lead{position:absolute;left:140px;top:72px;width:600px;font-size:11px;color:#4a3a20}
.cards{position:absolute;left:140px;top:130px;display:flex;gap:22px}
.card{width:216px;background:#fff;height:290px;position:relative}
.card-photo{height:150px;background:linear-gradient(160deg,#9fb4c8,#5f7486)}
.card h3{position:absolute;top:128px;left:0;width:150px;background:var(--blue);color:#fff;font-size:12px;padding:6px 10px}
.card p{font-size:10px;color:var(--muted);padding:18px 12px 8px}
.card .btn{position:absolute;left:12px;bottom:14px;width:80px;background:var(--blue);color:#fff;padding:6px 0;font-size:10px}

/* areas */
.areas{position:absolute;left:0;top:1683px;width:1200px;height:400px}
.areas-copy{position:absolute;left:50px;top:70px;width:400px}
.areas-copy h2{font-size:24px;font-weight:700;color:var(--blue);margin-bottom:10px}
.areas-copy h4{font-size:12px;font-style:italic;font-weight:700;color:var(--ink);margin-bottom:12px}
.areas-copy p{font-size:11px;color:var(--muted)}
.area-grid{position:absolute;left:490px;top:0;width:710px;height:400px;display:grid;grid-template-columns:repeat(3,1fr);grid-template-rows:repeat(2,1fr)}
.area{display:flex;align-items:center;justify-content:center;color:#fff;font-family:"Montserrat",sans-serif;font-weight:600;font-size:13px}
.area:nth-child(1){background:linear-gradient(135deg,#1d3f6b,#2f6fb0)}
.area:nth-child(2){background:linear-gradient(135deg,#2a7ac9,#6aa9e0)}
.area:nth-child(3){background:linear-gradient(135deg,#173555,#2d5a88)}
.area:nth-child(4){background:linear-gradient(135deg,#1a2430,#3a4652)}
.area:nth-child(5){background:linear-gradient(135deg,#202b38,#4b5866)}
.area:nth-child(6){background:linear-gradient(135deg,#151d27,#323e4b)}

/* testimonials */
.testimonials{position:absolute;left:0;top:2120px;width:1200px;height:320px}
.t-band{position:absolute;left:0;top:20px;width:500px;height:140px;background:var(--blue);padding:48px 0 0 50px;color:#fff;overflow:hidden}
.t-band h2{font-size:28px;font-weight:700}
.t-band p{font-size:11px}
.t-mark{position:absolute;right:30px;top:-8px;font-family:Georgia,serif;font-size:150px;color:rgba(255,255,255,.18);line-height:1}
.t-avatar{position:absolute;left:565px;top:60px;width:62px;height:62px;border-radius:50%;background:linear-gradient(135deg,#cbd5e1,#94a3b8)}
.t-quote{position:absolute;left:650px;top:58px;width:480px;font-size:11.5px;color:var(--muted)}
.t-quote strong{display:block;margin-top:8px;font-size:11px;color:var(--ink);font-style:italic}
.t-arrows{position:absolute;left:565px;top:150px;display:flex;gap:6px}
.t-arrows span{width:18px;height:18px;background:var(--blue);display:flex;align-items:center;justify-content:center}

/* footer */
.site-footer{position:absolute;left:0;top:2510px;width:1200px;height:294px;border-top:1px solid var(--line)}
.f-brand{position:absolute;left:48px;top:50px;width:260px}
.f-brand p{font-size:9px;color:var(--muted);margin-top:14px;width:230px}
.f-col{position:absolute;top:52px;font-size:10.5px;color:var(--muted);line-height:1.75}
.f-col h4{font-size:11px;color:var(--ink);font-weight:700;margin-bottom:6px}
.f-col .ic{display:inline-block;width:10px;height:10px;background:var(--blue);border-radius:2px;margin-right:6px;vertical-align:-1px}
.badges{position:absolute;left:1000px;top:52px}
.stars{display:flex;gap:3px;margin-bottom:10px}
.badge-row{display:flex;gap:8px}
.badge{width:60px;height:32px;background:var(--soft);border:1px solid var(--line)}
</style>
</head>
<body>

<header class="site-header">
  <div class="brand"><span class="brand-name">Steadfast Haulers</span></div>
  <div class="brand-tag">The Steadfast Haulers and Storage</div>
  <div class="topline">Call (555) 410-2297 &nbsp;|&nbsp; Brightcarryhaul.com</div>
  <nav class="main-nav">
    <span class="active">Home</span><span>About Us</span><span>Residential Moving</span><span>Services</span><span>Careers</span><span>Packing &amp; Supplies</span><span>Storage</span><span>Get a Quote</span>
  </nav>
</header>

<section class="hero">
  <div class="hero-photo" role="img" aria-label="Branded moving truck parked outside a suburban house"></div>
  <div class="hero-copy">
    <h1>We Help Move Lives Forward</h1>
    <p>Providing local &amp; long distance residential and commercial moving services since 2006</p>
  </div>
  <div class="call-box">
    <span>Call Today for Quote</span>
    <strong>(555) 410-2297</strong>
  </div>
</section>
<div class="hero-rule"></div>

<form class="quote-form">
  <h2>Get a <em>Free</em><br>Moving Quote!</h2>
  <div class="tabs">
    <div class="tab on"><i></i>Residential</div>
    <div class="tab"><i></i>Commercial</div>
    <div class="tab"><i></i>Storage</div>
  </div>
  <div class="field-row"><div class="field"><label>Moving From</label><div>Zip code</div></div><div class="field"><label>Moving To</label><div>Zip code</div></div></div>
  <div class="field-row"><div class="field"><label>Move Date</label><div>mm/dd/yyyy</div></div><div class="field"><label>Move Size</label><div>Select size</div></div></div>
  <div class="field-row"><div class="field"><label>Your Name</label><div>Full name</div></div></div>
  <div class="field-row"><div class="field"><label>Your Email Address</label><div>Email</div></div><div class="field"><label>Your Phone Number</label><div>Phone</div></div></div>
  <div class="form-actions"><span class="btn btn-orange">Free Quote</span><span class="btn btn-light">Make A Reservation</span></div>
</form>

<section class="about">
  <div class="about-panel"></div>
  <div class="about-photo" role="img" aria-label="Couple unpacking moving boxes in a new home"></div>
  <div class="about-copy">
    <h2>Moving Families &amp; Businesses<br>For Over A Decade</h2>
    <p>As a prominent moving company for the tri-state area, Steadfast Haulers is known for dependable, careful and affordable residential and commercial relocation services.</p>
    <p>We are proud of our trained crews, clean trucks and clear pricing. From a single room to a full office, we plan each move to fit your schedule and budget.</p>
  </div>
</section>

<section class="services">
  <h2>Moving Services</h2>
  <p class="lead">Every move is different, so we offer flexible services to fit your needs, whether you are moving across town or across the country.</p>
  <div class="cards">
    <article class="card"><div class="card-photo" role="img" aria-label="Movers loading household furniture"></div><h3>Residential Moving</h3><p>Careful packing and moving for homes and apartments of every size.</p><span class="btn">Read More</span></article>
    <article class="card"><div class="card-photo" role="img" aria-label="Office equipment being moved"></div><h3>Commercial Moving</h3><p>Planned office moves that keep your business running with little downtime.</p><span class="btn">Read More</span></article>
    <article class="card"><div class="card-photo" role="img" aria-label="Helper assisting a senior with packing"></div><h3>Senior Moving</h3><p>Patient, gentle help for seniors downsizing or moving closer to family.</p><span class="btn">Read More</span></article>
    <article class="card"><div class="card-photo" role="img" aria-label="Row of orange storage unit doors"></div><h3>Storage</h3><p>Clean, secure short and long term storage units for any belongings.</p><span class="btn">Read More</span></article>
  </div>
</section>

<section class="areas">
  <div class="areas-copy">
    <h2>Areas Served</h2>
    <h4>Our expansive network of offices provides us with a broad range of capabilities to best serve our customers' unique moving and storage needs.</h4>
    <p>We serve local towns and counties throughout the region, with crews ready for short local hops, long distance trips and storage. Tell us where you are going and we will plan the route.</p>
  </div>
  <div class="area-grid">
    <div class="area" role="img" aria-label="Coastal town skyline">Coastal</div>
    <div class="area" role="img" aria-label="Riverside city view">Riverside</div>
    <div class="area" role="img" aria-label="Harbor at dusk">Harbor</div>
    <div class="area" role="img" aria-label="Downtown street at night">Downtown</div>
    <div class="area" role="img" aria-label="City skyline at night">Metro</div>
    <div class="area" role="img" aria-label="Suburban avenue at night">Suburbs</div>
  </div>
</section>

<section class="testimonials">
  <div class="t-band"><span class="t-mark">&#8221;</span><h2>Testimonials</h2><p>What Customers Are Saying</p></div>
  <div class="t-avatar" role="img" aria-label="Customer portrait"></div>
  <div class="t-quote">
    Great service, fair prices and a friendly team. The crew arrived on time, wrapped all of our furniture with care and had everything set up in the new house before dinner. Highly recommended for any family move.
    <strong>Darren, Lakeview, CT</strong>
  </div>
  <div class="t-arrows">
    <span><svg width="8" height="8" viewBox="0 0 8 8"><path d="M6 0 2 4l4 4" fill="none" stroke="#fff" stroke-width="1.6"/></svg></span>
    <span><svg width="8" height="8" viewBox="0 0 8 8"><path d="M2 0l4 4-4 4" fill="none" stroke="#fff" stroke-width="1.6"/></svg></span>
  </div>
</section>

<footer class="site-footer">
  <div class="f-brand">
    <span class="brand-name">Steadfast Haulers</span>
    <p>&copy; 2024 The Steadfast Haulers and Storage. All rights reserved.</p>
  </div>
  <div class="f-col" style="left:390px">
    <h4>Headquarters</h4>
    The Steadfast Haulers and Storage<br>48 Harbor Point Road<br>Millbrook, CT 06400<br><br>Company ID 000000<br>Carrier No. 000000
  </div>
  <div class="f-col" style="left:620px">
    <h4>Moving Resources</h4>
    Moving Tips<br>Moving Checklist<br>Packing Guide<br>Moving Cost FAQ
  </div>
  <div class="f-col" style="left:800px">
    <h4>Connect With Us</h4>
    <span class="ic"></span>Community Page<br><span class="ic"></span>News Feed<br><span class="ic"></span>Photo Feed
  </div>
  <div class="badges">
    <div class="stars">
      <svg width="90" height="16" viewBox="0 0 90 16"><g fill="#f7a541"><path id="s" d="M8 0l2.4 5 5.4.6-4 3.7 1.1 5.4L8 12 3.1 14.7l1.1-5.4-4-3.7L5.6 5z"/><use href="#s" x="18"/><use href="#s" x="36"/><use href="#s" x="54"/><use href="#s" x="72"/></g></svg>
    </div>
    <div class="badge-row"><span class="badge"></span><span class="badge"></span></div>
  </div>
</footer>

</body>
</html>
```